New website for gluVista

We are looking to redesign our e-newsletter gluVista. This a monthly newsletter that publishes the latest research and product news in the diabetes field for people with diabetes. Our current website is here: www.gluvista-news.example.

The parameters are the new site must incorporate our logo, must use the same colors (variation in shade and adding some colors is fine, but the initial pallet should stay) and must be in 1024 by 768 px. It is crucially important that the font in the new design be easily readable (dark, well spaced). If it could be a layered PSD that would be ideal. We have attached 2 sketches of our own brainstorming for a potential lay-out for the home and a new issue page, but these are very rough and should not in any way limit the true designers out there.

We're envisioning a very polished, sophisticated looking magazine-esque site that presents a lot of information. When we were brainstorming for new site ideas we looked at major monthly publications such as the Harbor Ledger (www.harborledger.example) or Velvet Hour (www.vh-mag.example). Like these sites we would still like to feature much of our newest content on the front page, but in a manner that makes good use of space and feels uncluttered. Information needs to be clearly labeled and easy to find. In terms of the overall tone of the website, we do very much want it to be nice and elegant looking site, and one that is targeting a smart, engaged audience.
Updates

Reason: I didn't realize I'd made this due on a Sunday. Please take a couple of extra days everyone.

Industry/Entity Type

News

Requirements
Must have
• The logo. The same color scheme we currently use
Nice to have
• We like the idea of having a featured content box, of using hover buttons on top for our various sections, and potentially using a 3 column setup. However, we are not web designers, so the designer can use these suggestions at their discretion.

```html
<!DOCTYPE html>
<html lang="en">
<head>
<meta charset="utf-8">
<title>gluVista – research and product news for people with diabetes</title>
<link rel="stylesheet" href="https://fonts.googleapis.com/css2?family=Lato:ital,wght@0,400;0,700;0,900;1,700&family=Open+Sans:wght@400;600&family=PT+Sans+Narrow:wght@400;700&display=swap">
<style>
:root{
  --orange:#e55a1f;
  --orange-text:#e25a1c;
  --teal-logo:#4fa49c;
  --teal-footer:#6db3ad;
  --page:#cfe6e5;
  --panel:#dcefee;
  --tweet-box:#c3e1de;
  --tweet-inner:#dff0ee;
  --ink:#2b2b2b;
  --brown:#6b3a22;
  --login:#4a3a33;
  --gold:#f0b323;
  --dots:#b9cfcd;
  --white:#ffffff;
}
*{box-sizing:border-box;margin:0;padding:0}
html,body{width:1200px;height:900px;overflow:hidden;background:var(--page)}
.site{position:absolute;left:0;top:0;width:1024px;height:768px;transform:scale(1.171875);transform-origin:0 0;background:var(--page);font-family:"Lato",sans-serif;color:var(--ink);overflow:hidden}
.abs{position:absolute}

/* header */
.header{left:0;top:0;width:1024px;height:141px;background:linear-gradient(#ffffff,#f1f2f2)}
.brand{left:46px;top:36px;font-weight:400;font-size:50px;color:var(--teal-logo);letter-spacing:-1px;line-height:1}
.tagline{left:123px;top:95px;font-size:12px;color:var(--brown);letter-spacing:.2px;white-space:nowrap}
.brand-rule{left:46px;top:126px;width:171px;border-top:2px dotted var(--ink)}
.hero-art{left:462px;top:0;width:328px;height:141px;background:linear-gradient(110deg,#5fa9a3 0 14%,#e8e6e2 14% 60%,#e55a1f 60% 72%,#f1efec 72%)}
.signup{left:790px;top:30px;width:200px;height:90px}
.signup-brace{top:0;font-size:72px;line-height:80px;color:var(--gold)}
.signup-text{left:0;top:19px;width:200px;text-align:center;font-family:"PT Sans Narrow",sans-serif;font-size:15px;line-height:20px;color:#222;white-space:nowrap}
.signup-text b{font-weight:700}
.signup-dot{left:93px;top:-2px;width:12px;height:12px;border-radius:50%;background:var(--orange)}

/* nav */
.nav{left:0;top:141px;width:703px;height:33px;background:var(--orange);display:flex;align-items:center;padding-left:47px}
.nav a{color:var(--white);text-decoration:none;font-family:"Open Sans",sans-serif;font-size:12.5px;padding:0 11px;border-right:2px solid #f5b08f;line-height:20px}
.login{left:703px;top:141px;width:104px;height:33px;background:var(--login);color:#fff;font-family:"Open Sans",sans-serif;font-size:13px;text-align:center;line-height:33px}
.search-field{left:812px;top:145px;width:154px;height:23px;background:#fff;border:1px solid #c5cfcf;border-radius:5px}
.search-btn{left:968px;top:147px;width:46px;height:20px;background:linear-gradient(#fff,#e3e3e3);border:1px solid #c9c9c9;border-radius:8px;font-family:"Open Sans",sans-serif;font-size:9px;font-weight:600;text-align:center;line-height:18px;color:#222}

/* main panel */
.panel{left:40px;top:175px;width:663px;height:550px;background:var(--panel)}
.dot-row{height:0;border-top:3px dotted var(--dots)}
.thumb{width:86px;height:114px;background:#fff;border-radius:5px;padding:5px;box-shadow:0 1px 2px rgba(0,0,0,.12)}
.thumb span{display:block;width:100%;height:100%}
.story-title{font-style:italic;font-weight:700;font-size:11px;letter-spacing:1.4px;color:var(--orange-text);text-transform:uppercase;white-space:nowrap}
.story-text{font-size:11px;line-height:13.5px;letter-spacing:.6px;color:#222;white-space:nowrap}
.story-text b{font-weight:900}

/* sidebar */
.report{left:727px;top:188px;width:283px;height:121px;background:#fff;border-radius:0 60px 60px 0}
.report-cover{left:735px;top:195px;width:86px;height:106px;background:linear-gradient(#cfd8dc,#9fb6bf 55%,#7a8f6a);box-shadow:1px 1px 3px rgba(0,0,0,.3)}
.report-label{left:837px;top:198px;font-weight:700;font-size:19px;color:var(--orange-text);letter-spacing:-.3px;white-space:nowrap}
.report-title{left:838px;top:224px;font-weight:700;font-size:14.5px;line-height:18px;color:#333;white-space:nowrap}
.report-sub{left:838px;top:260px;font-size:10.5px;color:#333;white-space:nowrap}
.report-btn{left:842px;top:284px;width:139px;height:17px;background:var(--tweet-inner);font-size:10.5px;color:var(--orange-text);text-align:center;line-height:17px;white-space:nowrap}
.feed{left:727px;top:322px;width:195px;height:268px;background:var(--tweet-box)}
.feed-mark{left:743px;top:334px;width:24px;height:24px;background:#fff;border:1px solid #cfd8d8}
.feed-handle{left:774px;top:333px;font-size:8px;color:#333}
.feed-name{left:774px;top:343px;font-weight:900;font-size:11px;color:#222}
.feed-list{left:737px;top:365px;width:173px;height:215px;background:var(--tweet-inner);padding:4px 5px}
.tweet{font-size:8.5px;line-height:10.5px;color:#555;padding:1px 0 5px;border-bottom:1px solid #c9dedc;margin-bottom:6px;white-space:nowrap}
.tweet:last-child{border:none}
.tweet .link{color:#2a8bb5;font-weight:700}
.tweet .meta{display:block;color:#4aa7c4;font-size:7px}
.success{left:725px;top:603px;width:273px;height:107px;background:#f4f9f9;border-radius:12px}
.success-label{left:742px;top:615px;font-weight:700;font-size:19px;color:var(--orange-text);white-space:nowrap}
.success-text{left:743px;top:640px;font-size:10.5px;line-height:12.5px;color:#222;white-space:nowrap}
.success-more{left:743px;top:681px;font-size:10.5px;color:#222}
.success-thumb{left:913px;top:613px;width:67px;height:86px;background:#fff;padding:4px;border-radius:3px}
.success-thumb span{display:block;width:100%;height:100%;background:linear-gradient(#f2d14b,#e3a24f 60%,#d8776b)}

/* footer */
.footer{left:0;top:727px;width:1024px;height:41px;background:var(--teal-footer);color:#fff;font-family:"Open Sans",sans-serif;font-size:11px;text-align:center;line-height:44px;white-space:nowrap}
</style>
</head>
<body>
<div class="site">
  <header class="header abs">
    <div class="brand abs">gluVista</div>
    <div class="tagline abs">research and product news for people with diabetes</div>
    <div class="brand-rule abs"></div>
    <div class="hero-art abs" role="img" aria-label="Collage of a molecule model, a syringe and a medicine vial framed by teal and orange chevrons"></div>
    <div class="signup abs">
      <div class="signup-brace abs" style="left:-4px">{</div>
      <div class="signup-brace abs" style="left:180px">}</div>
      <div class="signup-dot abs"></div>
      <div class="signup-text abs"><b>SIGN-UP FOR GLUVISTA</b><br>CLICK HERE TO SIGN-UP<br>FOR GLUVISTA. <b>IT'S FREE!</b></div>
    </div>
  </header>

  <nav class="nav abs">
    <a>HOME</a><a>ISSUES</a><a>COLUMNS</a><a>TOPICS</a><a>ABOUT US</a>
  </nav>
  <div class="login abs">Client Login</div>
  <div class="search-field abs"></div>
  <div class="search-btn abs">Search</div>

  <main class="panel abs"></main>

  <div class="dot-row abs" style="left:55px;top:212px;width:312px"></div>
  <div class="dot-row abs" style="left:379px;top:212px;width:312px"></div>
  <div class="dot-row abs" style="left:55px;top:338px;width:312px"></div>
  <div class="dot-row abs" style="left:379px;top:338px;width:312px"></div>
  <div class="dot-row abs" style="left:55px;top:465px;width:312px"></div>
  <div class="dot-row abs" style="left:379px;top:465px;width:312px"></div>
  <div class="dot-row abs" style="left:55px;top:591px;width:312px"></div>
  <div class="dot-row abs" style="left:379px;top:591px;width:312px"></div>
  <div class="dot-row abs" style="left:149px;top:705px;width:218px"></div>
  <div class="dot-row abs" style="left:473px;top:705px;width:218px"></div>

  <!-- left column -->
  <div class="thumb abs" style="left:54px;top:219px"><span role="img" aria-label="Portrait photo of the editor" style="background:linear-gradient(#d9b9a0,#8a5a45)"></span></div>
  <div class="story-title abs" style="left:149px;top:251px">From the Editor</div>
  <div class="story-text abs" style="left:149px;top:277px"><b>MARA</b> muses on the search for a cure,<br>and what we have in the meantime.</div>

  <div class="thumb abs" style="left:54px;top:345px"><span role="img" aria-label="Photo of a mother hugging her daughter" style="background:linear-gradient(#e8c9a6,#d09a7a 60%,#e6d6d8)"></span></div>
  <div class="story-title abs" style="left:149px;top:377px">Learning Curve</div>
  <div class="story-text abs" style="left:149px;top:403px">Where are we today in the quest<br>for a cure?</div>

  <div class="thumb abs" style="left:54px;top:471px"><span role="img" aria-label="Photo of an insulin pump clipped to a belt" style="background:linear-gradient(#d47a3a,#5c5a3c)"></span></div>
  <div class="story-title abs" style="left:149px;top:499px">New Now Next</div>
  <div class="story-text abs" style="left:149px;top:515px;line-height:18px">An update on the artificial pancreas,<br>new drugs in development, Glyquent’s<br>approval in Europe, and more...</div>

  <div class="thumb abs" style="left:54px;top:597px"><span role="img" aria-label="Portrait photo of the columnist" style="background:linear-gradient(#c9a287,#8a6248)"></span></div>
  <div class="story-title abs" style="left:149px;top:622px">Sum Musings</div>
  <div class="story-text abs" style="left:149px;top:648px">What does a cure mean to you?<br><b>Lena Marsh</b> Calder shares her<br>thoughts.</div>

  <!-- right column -->
  <div class="thumb abs" style="left:379px;top:219px"><span role="img" aria-label="Photo of a glass medicine vial" style="background:linear-gradient(#f4f6f6,#c7d0d0)"></span></div>
  <div class="story-title abs" style="left:473px;top:255px">Quotable Quotes</div>
  <div class="story-text abs" style="left:473px;top:281px">(S)he said what?!?</div>

  <div class="thumb abs" style="left:379px;top:345px"><span role="img" aria-label="Portrait photo of the columnist" style="background:linear-gradient(#d3c2b4,#5e4d45)"></span></div>
  <div class="story-title abs" style="left:473px;top:364px">Thinking like a Pancreas</div>
  <div class="story-text abs" style="left:473px;top:390px">What if a closed-loop system used<br>three hormones, instead of one?<br><b>Daniel Ostrow</b> discusses<br>the possibility.</div>

  <div class="thumb abs" style="left:379px;top:471px"><span role="img" aria-label="Photo of a researcher working in a laboratory" style="background:linear-gradient(#c9d7df,#5d7182)"></span></div>
  <div class="story-title abs" style="left:473px;top:489px">Trial Watch</div>
  <div class="story-text abs" style="left:473px;top:515px">Could diabetes education at an eye<br>doctor visit improve glycemic control?<br>Could Exavia be used in type 1<br>diabetes?</div>

  <div class="thumb abs" style="left:379px;top:597px"><span role="img" aria-label="Photo of a climber on a cliff above the sea" style="background:linear-gradient(#8fb9da,#3b6f9a 60%,#3a4a55)"></span></div>
  <div class="story-title abs" style="left:473px;top:635px">Fingersticks</div>
  <div class="story-text abs" style="left:473px;top:661px">A goal within reach...</div>

  <!-- sidebar -->
  <aside>
    <div class="report abs"></div>
    <div class="report-cover abs" role="img" aria-label="Cover of the report showing a mother and child by the sea"></div>
    <div class="report-label abs">FREE REPORT</div>
    <div class="report-title abs">Chasing a cure<br>for type 1 Diabetes:</div>
    <div class="report-sub abs">How long will we have to wait?</div>
    <div class="report-btn abs">Click here to read our report!</div>

    <div class="feed abs"></div>
    <div class="feed-mark abs"></div>
    <div class="feed-handle abs">gluvista</div>
    <div class="feed-name abs">gluVistaNews</div>
    <div class="feed-list abs">
      <div class="tweet">Norvalis’s GPR40 agonist,NVX-410,<br>reduced A1c by 1% w/ few side effects<br>or instances of hypoglycemia- see<br><span class="link">http://lnk.example/Bk4X3g</span><span class="meta">about 1 hour ago · reply · retweet · favorite</span></div>
      <div class="tweet">“Chasing a Cure is a<br>comprehensive,but easy to read<br>summation,a gift to all with<br>diabetes”Paul Brenner @sugarwise -<br>see <span class="link">http://lnk.example/Xg6N6t</span><span class="meta">3 hours ago · reply · retweet · favorite</span></div>
      <div class="tweet">T1DM afflicts 3 million Americans-<br>educate yourself on the possible cures.<br>Click lnk.example/nG4f to download the<br>free Chasing a Cure Report<span class="meta">5 hours ago · reply · retweet · favorite</span></div>
    </div>

    <div class="success abs"></div>
    <div class="success-label abs">Success Story</div>
    <div class="success-text abs">Lorem ipsum dolor sit amet,<br>adipiscing elit. Morbi commodo,<br>ipsum sed pharetra...</div>
    <div class="success-more abs">more...</div>
    <div class="success-thumb abs"><span role="img" aria-label="Photo of a smiling young girl"></span></div>
  </aside>

  <footer class="footer abs">HOME &nbsp;|&nbsp; PRIVACY POLICY &nbsp;|&nbsp; EDITORIAL POLICY/DISCLOSURE &nbsp;|&nbsp; CONTACT US © 2011 GLUVISTA®. ALL RIGHTS RESERVED.</footer>
</div>
</body>
</html>
```